Webdesign für Online-Shop für Honig
Zielgruppe
Verkauf von Sidr Honig. Ein sehr hochwertiger Premium-Honig aus dem Jemen.
Aufgabenstellung
Zu Erstellen ist ein Design für einen Onlineshop. Der Onlineshop verkauft Kosmetik-, Lebensmittel- und Gesundheitsprodukte die alle auf einem Honig basieren.
Domain: qalvenu.com
Die Seite soll sehr hochwertig und orientalisch wirken. Der Hintergrund soll auf jeden Fall dunkel sein.
Wir benötigen ein Screendesign der:
- Home-Seite,
- Über uns-Seite
- Produktdetailseite.
Die Designs müssen nicht per HTML umgesetzt werden, können aber. Es reicht ein reines Design als Bild, HTML ist aber auch in Ordnung.
Bitte hochwertige Stockbilder nutzen.

```html
<!DOCTYPE html>
<html lang="de">
<head>
<meta charset="utf-8">
<title>QALVENU Premium Honey</title>
<link href="https://fonts.googleapis.com/css2?family=Cormorant+Garamond:wght@400;500&family=EB+Garamond:wght@400&family=Great+Vibes&family=Montserrat:wght@400&display=swap" rel="stylesheet">
<style>
  :root {
    --bg: #000000;
    --gold: #c8935f;
    --gold-soft: #b9895a;
    --ornament: #3b2a18;
    --amber-light: #f0b040;
    --amber-deep: #7a3c08;
  }
  * { margin: 0; padding: 0; box-sizing: border-box; }
  html, body { width: 1200px; height: 3099px; overflow: hidden; background: var(--bg); }
  .page { position: relative; width: 1200px; height: 3099px; background: var(--bg); color: var(--gold); font-family: "EB Garamond", Georgia, serif; }
  .abs { position: absolute; }

  .ornament { position: absolute; border-radius: 50%; background: radial-gradient(circle, rgba(59,42,24,0.55) 0%, rgba(59,42,24,0.35) 55%, rgba(0,0,0,0) 72%); }
  .ornament--left { left: -300px; top: 60px; width: 640px; height: 720px; }
  .ornament--right { left: 860px; top: 60px; width: 660px; height: 730px; }
  .ornament--footer { left: 277px; top: 2732px; width: 650px; height: 650px; }

  .nav-cart { left: 974px; top: 80px; }
  .nav-menu { left: 1035px; top: 86px; }

  .brand { left: 0; width: 1200px; top: 205px; text-align: center; }
  .brand__name { font-family: "Cormorant Garamond", Georgia, serif; font-weight: 500; font-size: 62px; line-height: 66px; letter-spacing: 1px; color: var(--gold); }
  .brand__tag { font-family: "Montserrat", Arial, sans-serif; font-size: 14px; letter-spacing: 3.5px; color: var(--gold); margin-top: 4px; }

  .tagline { left: 0; width: 1200px; top: 390px; text-align: center; font-family: "Great Vibes", cursive; font-size: 68px; color: var(--gold); }

  .headline { font-family: "Cormorant Garamond", Georgia, serif; font-weight: 400; font-size: 122px; line-height: 113px; color: var(--gold); text-transform: uppercase; }
  .headline--intro { left: -6px; top: 600px; }
  .headline--gold { left: 562px; top: 1290px; }

  .mark-dot { left: 562px; top: 686px; width: 15px; height: 15px; border: 1.5px solid var(--gold); border-radius: 50%; }

  .body-text { font-size: 14.5px; line-height: 22.5px; color: var(--gold); }
  .intro-text { left: 562px; top: 720px; width: 372px; }

  .photo { position: absolute; }
  .photo--pour { left: 143px; top: 1145px; width: 336px; height: 442px; background: linear-gradient(160deg, #3a2450 0%, #b86a12 35%, var(--amber-light) 55%, #d9c27a 80%, #e8d89a 100%); }
  .photo--spoon { left: 567px; top: 1814px; width: 336px; height: 428px; background: radial-gradient(ellipse at 55% 50%, #f0a020 0%, #a85a08 30%, #2a1604 62%, #0a0604 100%); }
  .photo-frame { position: absolute; border: 1px solid var(--gold-soft); }
  .photo-frame--pour { left: 156px; top: 1162px; width: 338px; height: 440px; }
  .photo-frame--spoon { left: 584px; top: 1796px; width: 334px; height: 427px; }

  .script { font-family: "Great Vibes", cursive; color: var(--gold); }
  .script--liquid { left: 80px; top: 1568px; font-size: 64px; line-height: 64px; }
  .script--liquid span { display: block; padding-left: 40px; }
  .script--tasty { left: 794px; top: 2218px; font-size: 66px; }

  .caption-pour { left: 253px; top: 1616px; width: 110px; }
  .caption-spoon { left: 935px; top: 1790px; width: 130px; }

  .feature { position: absolute; top: 2385px; width: 270px; text-align: center; }
  .feature--healthy { left: 132px; }
  .feature--beauty { left: 465px; }
  .feature--tasty { left: 799px; }
  .feature__icon { display: block; margin: 0 auto; width: 86px; height: 86px; border-radius: 50%; background: radial-gradient(circle, rgba(200,147,95,0.28) 0%, rgba(200,147,95,0.08) 70%, rgba(0,0,0,0) 72%); }
  .feature__title { font-family: "Cormorant Garamond", Georgia, serif; font-size: 45px; font-weight: 400; line-height: 50px; margin-top: 20px; color: var(--gold); }
  .feature__text { margin-top: 28px; font-size: 14.5px; line-height: 22.5px; }
  .feature__button { display: inline-block; margin-top: 34px; width: 91px; height: 34px; border: 1px solid var(--gold-soft); font-size: 19px; line-height: 31px; color: var(--gold); text-decoration: none; }

  .footer-rule { left: 130px; top: 2849px; width: 937px; border-top: 2px dotted var(--gold-soft); }
  .footer-mark { left: 135px; top: 2912px; width: 54px; height: 54px; border: 1.5px solid var(--gold); border-radius: 50%; }
  .footer-col { top: 2913px; font-size: 14.5px; line-height: 23px; color: var(--gold); }
  .footer-col--address { left: 238px; }
  .footer-col--links { left: 527px; }
  .footer-col--legal { left: 744px; }

  .to-top { left: 1099px; top: 2994px; }
</style>
</head>
<body>
<div class="page">
  <div class="ornament ornament--left" role="img" aria-label="Orientalisches Mandala-Ornament, dunkel goldbraun"></div>
  <div class="ornament ornament--right" role="img" aria-label="Orientalisches Mandala-Ornament, dunkel goldbraun"></div>
  <div class="ornament ornament--footer" role="img" aria-label="Orientalisches Mandala-Ornament im Fußbereich"></div>

  <svg class="abs nav-cart" width="26" height="28" viewBox="0 0 26 28" aria-label="Warenkorb">
    <rect x="3" y="8" width="20" height="18" fill="none" stroke="#c8935f" stroke-width="2"/>
    <path d="M8 8 V5 a5 5 0 0 1 10 0 V8" fill="none" stroke="#c8935f" stroke-width="2"/>
  </svg>
  <svg class="abs nav-menu" width="64" height="20" viewBox="0 0 64 20" aria-label="Menü">
    <line x1="0" y1="1" x2="64" y2="1" stroke="#c8935f" stroke-width="2"/>
    <line x1="0" y1="9" x2="64" y2="9" stroke="#c8935f" stroke-width="2"/>
    <line x1="8" y1="17" x2="64" y2="17" stroke="#c8935f" stroke-width="2"/>
  </svg>

  <header class="abs brand">
    <div class="brand__name">QALVENU</div>
    <div class="brand__tag">PREMIUM HONEY</div>
  </header>

  <p class="abs tagline">more than just a honey</p>

  <h1 class="abs headline headline--intro">More<br>than<br>just a<br>honey</h1>

  <div class="abs mark-dot"></div>
  <p class="abs body-text intro-text">Lorem ipsum dolor sit amet, conLorem ipsum dolor sit amet, consectetuer adipiscing elit, sed diam nonummy nibh euismod tincidunt ut laoreet dolore magna aliquam erat volutpat. Ut wisi enim ad minim veniam, quis nostrud exerci tation ullamcorper suscipit lobortis nisl ut aliquip ex ea commodo consequat. Duis autem vel Lorem ipsum dolor sit amet, consectetuer adipiscing elit, sed diam nonummy nibh euismod tincidunt ut laoreet dolore magna aliquam erat volutpat. Ut wisi enim ad minim veniam, quis nostrud exerci tation ullamcorper suscipit lobortis nisl ut aliquip ex ea commodo consequat. Duis autem vel eum iriure dolor in hendrerit in vulputate velit esse molestie consequat, vel illum dolore eu feugiat nulla facilisis at vero eros et accumsan et iusto odio dignissim qui blandit praesent luptatum zzril delenit augue duis dolore te feugait nulla facilisi. Lorem ipsum dolor sit amet, cons ectetuer adipiscing elit, seortis nisl ut aliquip ex ea commodo consequat. Lorem ipsum dolor sit amet, consectetuer adipiscing elit, sed diam nonummy nibh euismod tincidunt ut laoreet dolore magna aliquam erat volutpat. Ut wisi enim ad minim veniam, quis nostrud</p>

  <div class="photo-frame photo-frame--pour"></div>
  <div class="photo photo--pour" role="img" aria-label="Foto: goldener Honig fließt in einem Strahl mit Lichtreflexen"></div>
  <p class="abs script script--liquid">liquid<span>gold</span></p>
  <p class="abs body-text caption-pour">Veniam, tion ullamcorper suscipit lob.</p>

  <h2 class="abs headline headline--gold">Liquid<br>gold<br>from<br>Jemen</h2>

  <div class="photo-frame photo-frame--spoon"></div>
  <div class="photo photo--spoon" role="img" aria-label="Foto: Honig tropft von einem Löffel vor dunklem Hintergrund"></div>
  <p class="abs body-text caption-spoon">Ut wisi enim ad minim veniam, tion ullamcorper suscipit lob.</p>
  <p class="abs script script--tasty">tasty</p>

  <section class="feature feature--healthy">
    <span class="feature__icon" role="img" aria-label="Symbol: Herz mit Waben"></span>
    <h3 class="feature__title">HEALTHY</h3>
    <p class="feature__text">Dolor sit amet, conLorem ipsum dolor sit amet, consectetuer adipiscing elit, sed diam nonummy sit amet,nibh euismod tincidu.</p>
    <a class="feature__button" href="#">more</a>
  </section>
  <section class="feature feature--beauty">
    <span class="feature__icon" role="img" aria-label="Symbol: Hand mit Honigtropfen"></span>
    <h3 class="feature__title">BEAUTY</h3>
    <p class="feature__text">Lorem ipsum dolor sit amet, conLorem ipsum dolor sit amet, consectetuer adipiscing elit, sed diam nonummy nibh euismod tincidper suscipit</p>
    <a class="feature__button" href="#">more</a>
  </section>
  <section class="feature feature--tasty">
    <span class="feature__icon" role="img" aria-label="Symbol: Honiglöffel"></span>
    <h3 class="feature__title">TASTY</h3>
    <p class="feature__text">Ipsum dolor sit amet, conLorem ipsum dolor sit amet, consectetuer adipiscing enim ad minim veniam, quis nostrud exerci tation ullamc.</p>
    <a class="feature__button" href="#">more</a>
  </section>

  <div class="abs footer-rule"></div>
  <div class="abs footer-mark"></div>
  <div class="abs footer-col footer-col--address">QALVENU PREMIUM HONEY<br>Street Number 123<br>1234 City</div>
  <div class="abs footer-col footer-col--links">Healthy<br>Beauty<br>Tasty</div>
  <div class="abs footer-col footer-col--legal">Impressum<br>AGB</div>

  <svg class="abs to-top" width="60" height="60" viewBox="0 0 60 60" aria-label="Nach oben">
    <circle cx="30" cy="30" r="28.5" fill="none" stroke="#c8935f" stroke-width="1.5"/>
    <polyline points="15,37 30,22 45,37" fill="none" stroke="#c8935f" stroke-width="1.5"/>
  </svg>
</div>
</body>
</html>
```